Upscale business cards needed for family office

We would like professional business cards created for employees of our family office. Relatively simple and straightforward, but also with a unique element to set them apart. Probably stick with neutral and simple colors that mesh well with the colors in the logo. We need space for the traditional elements, including name, title, address, email/phone number.

Industry/Entity Type

Business

Contact Information for Business Card

Space for name, title, phone number, email, address

```html
<!DOCTYPE html>
<html lang="en">
<head>
<meta charset="utf-8">
<title>Daniel Reyes — Business Card</title>
<link rel="stylesheet" href="https://fonts.googleapis.com/css2?family=Tinos:wght@400&display=swap">
<style>
  :root {
    --page: #e9e6e1;
    --card-black: #0b0b0c;
    --card-black-hi: #2a2a2d;
    --card-blue: #3d72b4;
    --card-blue-dark: #2e5c99;
    --ink-light: #ffffff;
    --ink-soft: #e6eef8;
    --frame-grey: #9a9a9a;
  }
  * { box-sizing: border-box; margin: 0; padding: 0; }
  html, body {
    width: 1200px; height: 1022px; overflow: hidden;
    background: var(--page);
    font-family: "Tinos", "Times New Roman", serif;
  }
  .sheet {
    width: 1200px; height: 1022px;
    display: flex; flex-direction: column;
    align-items: center; justify-content: center; gap: 64px;
  }
  .card {
    width: 630px; height: 360px;
    border-radius: 22px;
    position: relative; overflow: hidden;
    box-shadow: 0 10px 28px rgba(0,0,0,.25);
  }
  /* Front */
  .card--front {
    background: linear-gradient(160deg, var(--card-black-hi) 0%, var(--card-black) 55%);
    display: flex; align-items: center; justify-content: center;
  }
  .brand {
    display: flex; flex-direction: column; align-items: center; gap: 18px;
  }
  .brand__row { display: flex; align-items: center; gap: 16px; }
  .brand__square {
    width: 26px; height: 26px;
    border: none; background: var(--card-blue);
  }
  .brand__name {
    color: var(--ink-light);
    font-size: 46px; letter-spacing: 1px;
  }
  .brand__person {
    color: var(--ink-light);
    font-size: 22px; letter-spacing: 2px; text-transform: uppercase;
  }
  /* Back */
  .card--back {
    background: linear-gradient(170deg, #4a80c2 0%, var(--card-blue) 45%, var(--card-blue-dark) 100%);
  }
  .card__rule {
    position: absolute; left: 0; top: 0; bottom: 0; width: 6px;
    background: var(--ink-light);
  }
  .contact {
    position: absolute; left: 250px; top: 58px;
    color: var(--ink-light);
  }
  .contact__name {
    font-size: 27px; letter-spacing: 1px; text-transform: uppercase;
  }
  .contact__title { font-size: 17px; color: var(--ink-soft); margin-top: 4px; }
  .contact__address { font-size: 17px; line-height: 1.5; margin-top: 20px; }
  .contact__list { list-style: none; margin-top: 16px; font-size: 17px; line-height: 1.7; }
  .contact__list li { display: flex; align-items: center; gap: 12px; }
  .contact__icon { width: 14px; height: 14px; flex: none; }
</style>
</head>
<body>
<main class="sheet">
  <section class="card card--front" aria-label="Card front">
    <div class="brand">
      <div class="brand__row">
        <span class="brand__square"></span>
        <span class="brand__name">Reyes &amp; Co.</span>
      </div>
      <span class="brand__person">Daniel Reyes</span>
    </div>
  </section>

  <section class="card card--back" aria-label="Card back">
    <div class="card__rule"></div>
    <div class="contact">
      <h1 class="contact__name">Daniel Reyes</h1>
      <p class="contact__title">Director</p>
      <p class="contact__address">2281 Harbor Lane<br>Fairview CA 90210</p>
      <ul class="contact__list">
        <li>
          <svg class="contact__icon" viewBox="0 0 16 16" aria-hidden="true"><path fill="#fff" d="M4 1l2.5 3-1.5 1.5c.8 2 2.5 3.7 4.5 4.5L11 8.5l3 2.5-1.5 3C7 14 2 9 2 2.5z"/></svg>
          +330 555-0142
        </li>
        <li>
          <svg class="contact__icon" viewBox="0 0 16 16" aria-hidden="true"><rect x="1.5" y="3.5" width="13" height="9" fill="none" stroke="#fff" stroke-width="1.4"/><path d="M1.5 3.5l6.5 5 6.5-5" fill="none" stroke="#fff" stroke-width="1.4"/></svg>
          info@danielreyes.com
        </li>
        <li>
          <svg class="contact__icon" viewBox="0 0 16 16" aria-hidden="true"><circle cx="8" cy="8" r="6.5" fill="none" stroke="#fff" stroke-width="1.3"/><ellipse cx="8" cy="8" rx="3" ry="6.5" fill="none" stroke="#fff" stroke-width="1.1"/><path d="M1.5 8h13" stroke="#fff" stroke-width="1.1"/></svg>
          www.danielreyes.com
        </li>
      </ul>
    </div>
  </section>
</main>
</body>
</html>
```